Bref créative
Letterhead, envelope, business card design
Marlowe Crest Advisory
I need double sided standard sized Business Card [3.5" x 2"]
Use whatever font you think is best
Professional
R. Dwight Folsom, DWMA®
Wealth Advisor
2400 Birchmoor Avenue
Suite 418
Delford, PA 19586
rfolsom@marlowe-crest.example
www.marlowe-crest.example
The following disclosure goes on letterhead at the bottom, on the back of the envelope on the flap, and on the business card.
Securities offered through QVD Brokerage, Member NAXO/BTPE.
Investment advice offered through Harbor Counsel Partners, a registered investment advisor.
Harbor Counsel Partners and Marlowe Crest Advisory are separate entities from QVD Brokerage.
You can either design a one sided business card or a two sided business card. If you design a two sided card, follow these guidelines:
1. Place the address on the back of the card along with the disclosure. Logo, name and title can remain on the front side of the card. OR
2. Place the disclosure on the front of the card and move “nonessential” information such as website address, fax number, etc. to the back.
Existing logo files

```html
<!DOCTYPE html>
<html lang="en">
<head>
<meta charset="utf-8">
<title>Marlowe Crest Advisory — Stationery Set</title>
<link href="https://fonts.googleapis.com/css2?family=Libre+Baskerville:wght@400;700&family=Open+Sans:wght@400;600&display=swap" rel="stylesheet">
<style>
  :root {
    --backdrop: #e9e4dc;
    --paper: #ffffff;
    --navy: #1b3a66;
    --navy-deep: #0f2547;
    --blue-mid: #3f6aa3;
    --gold: #c9a24a;
    --gold-light: #e8d08a;
    --ink: #4a4a4a;
    --shadow: 0 2px 5px rgba(0,0,0,.22);
  }
  * { box-sizing: border-box; margin: 0; padding: 0; }
  html, body { width: 1200px; height: 422px; overflow: hidden; }
  body {
    background: var(--backdrop);
    position: relative;
    font-family: "Open Sans", Arial, sans-serif;
    color: var(--ink);
  }
  .sheet { position: absolute; background: var(--paper); box-shadow: var(--shadow); overflow: hidden; }

  .brand { display: flex; align-items: center; gap: 4px; }
  .brand-mark { width: 9px; height: 9px; background: var(--navy); flex: none; }
  .brand-name {
    font-family: "Libre Baskerville", Georgia, serif;
    font-weight: 700; color: var(--navy);
    text-transform: uppercase; letter-spacing: .04em; line-height: 1.05;
    font-size: 9px;
  }
  .brand--light .brand-mark { background: var(--gold); }
  .brand--light .brand-name { color: var(--paper); }

  .fine { font-size: 3.6px; line-height: 1.35; }
  .disclosure { font-size: 3.6px; line-height: 1.4; color: var(--gold); text-align: center; }

  /* Business cards */
  .card { width: 134px; height: 55px; }
  .card--front { left: 124px; top: 64px; padding: 8px 9px; }
  .card--front .bar { position: absolute; left: 0; right: 0; bottom: 8px; height: 10px;
    background: linear-gradient(90deg, var(--navy-deep), var(--blue-mid)); }
  .card--front .bar::after { content: ""; position: absolute; left: 0; right: 0; top: -2px; height: 2px; background: var(--gold); }
  .card--front .contact { position: absolute; left: 9px; top: 26px; color: var(--navy); }

  .card--back { left: 124px; top: 142px; width: 84px; padding: 5px 6px; }
  .card--back .band { position: absolute; left: 0; right: 0; top: 18px; height: 12px;
    background: linear-gradient(90deg, var(--gold), var(--gold-light)); }
  .card--back .person { position: absolute; left: 6px; top: 20px; font-size: 4.2px; color: var(--navy-deep); font-weight: 600; }
  .card--back .address { position: absolute; left: 6px; top: 35px; color: var(--navy); }

  .card--blue { left: 214px; top: 142px; width: 104px; height: 62px; padding: 10px;
    background: linear-gradient(135deg, var(--navy-deep), var(--blue-mid)); }
  .card--blue .brand { margin-top: 12px; }
  .card--blue .brand-name { font-size: 7px; }
  .card--blue .rule { position: absolute; left: 0; right: 0; bottom: 10px; height: 2px; background: var(--gold); }

  /* Envelope back, left */
  .envelope-back { left: 91px; top: 290px; width: 222px; height: 122px; }
  .flap { position: absolute; inset: 0; }
  .envelope-back .disclosure-block { position: absolute; left: 40px; right: 40px; top: 12px; color: var(--navy); font-size: 3.3px; text-align: center; line-height: 1.4; }
  .envelope-back .brand { position: absolute; left: 50%; top: 80px; transform: translateX(-50%); flex-direction: column; gap: 2px; }
  .envelope-back .brand-name { font-size: 6px; text-align: center; }

  /* Letterheads */
  .letterhead { top: 19px; width: 259px; height: 375px; padding: 16px 18px; }
  .letterhead--one { left: 330px; }
  .letterhead--two { left: 606px; }
  .letterhead .top { display: flex; justify-content: space-between; }
  .letterhead .brand-name { font-size: 8.5px; }
  .letterhead .address { text-align: left; color: var(--navy); width: 62px; }
  .letterhead .disclosure { position: absolute; left: 30px; right: 30px; bottom: 14px; }
  .letterhead .footer-line { position: absolute; left: 30px; right: 30px; bottom: 34px; height: 1px; background: var(--gold); }

  /* Envelope front */
  .envelope-front { left: 883px; top: 79px; width: 300px; height: 161px; padding: 12px 14px; }
  .envelope-front .address { margin-top: 4px; margin-left: 13px; color: var(--navy); }
  .envelope-front .stripe { position: absolute; left: 0; right: 0; bottom: 18px; height: 12px;
    background: linear-gradient(90deg, var(--paper) 0%, var(--blue-mid) 35%, var(--navy-deep) 100%); }
  .envelope-front .stripe::after { content: ""; position: absolute; left: 0; right: 0; bottom: -3px; height: 2px;
    background: linear-gradient(90deg, var(--paper) 10%, var(--gold) 60%); }

  /* Envelope back, right */
  .envelope-back-plain { left: 883px; top: 281px; width: 300px; height: 131px; }
  .envelope-back-plain .disclosure-block { position: absolute; left: 80px; right: 80px; top: 52px; font-size: 3.3px; color: var(--navy); text-align: center; line-height: 1.4; }
</style>
</head>
<body>

  <!-- Business card front -->
  <section class="sheet card card--front">
    <div class="brand"><span class="brand-mark"></span><span class="brand-name">Marlowe Crest<br>Advisory</span></div>
    <div class="contact fine">R. Dwight Folsom, DWMA®<br>Wealth Advisor<br>rfolsom@marlowe-crest.example</div>
    <div class="bar"></div>
  </section>

  <!-- Business card back -->
  <section class="sheet card card--back">
    <div class="band"></div>
    <div class="person">R. Dwight Folsom, DWMA®</div>
    <div class="address fine">2400 Birchmoor Avenue, Suite 418<br>Delford, PA 19586</div>
  </section>

  <!-- Business card, navy variant -->
  <section class="sheet card card--blue">
    <div class="brand brand--light"><span class="brand-mark"></span><span class="brand-name">Marlowe Crest Advisory</span></div>
    <div class="rule"></div>
  </section>

  <!-- Envelope, back view with flap -->
  <section class="sheet envelope-back">
    <svg class="flap" viewBox="0 0 222 122" preserveAspectRatio="none">
      <polyline points="0,0 111,58 222,0" fill="none" stroke="#cfcfcf" stroke-width="0.8"/>
    </svg>
    <p class="disclosure-block">Securities offered through QVD Brokerage, Member NAXO/BTPE. Investment advice offered through Harbor Counsel Partners, a registered investment advisor. Harbor Counsel Partners and Marlowe Crest Advisory are separate entities from QVD Brokerage.</p>
    <div class="brand"><span class="brand-mark"></span><span class="brand-name">Marlowe Crest Advisory</span></div>
  </section>

  <!-- Letterhead -->
  <section class="sheet letterhead letterhead--one">
    <div class="top">
      <div class="brand"><span class="brand-mark"></span><span class="brand-name">Marlowe Crest<br>Advisory</span></div>
      <div class="address fine">2400 Birchmoor Avenue<br>Suite 418<br>Delford, PA 19586<br>rfolsom@marlowe-crest.example<br>www.marlowe-crest.example</div>
    </div>
    <div class="footer-line"></div>
    <p class="disclosure">Securities offered through QVD Brokerage, Member NAXO/BTPE. Investment advice offered through Harbor Counsel Partners, a registered investment advisor. Harbor Counsel Partners and Marlowe Crest Advisory are separate entities from QVD Brokerage.</p>
  </section>

  <!-- Letterhead, second variant -->
  <section class="sheet letterhead letterhead--two">
    <div class="top">
      <div class="brand"><span class="brand-mark"></span><span class="brand-name">Marlowe Crest<br>Advisory</span></div>
      <div class="address fine">2400 Birchmoor Avenue<br>Suite 418<br>Delford, PA 19586<br>rfolsom@marlowe-crest.example<br>www.marlowe-crest.example</div>
    </div>
    <p class="disclosure" style="color: var(--navy);">Securities offered through QVD Brokerage, Member NAXO/BTPE. Investment advice offered through Harbor Counsel Partners, a registered investment advisor. Harbor Counsel Partners and Marlowe Crest Advisory are separate entities from QVD Brokerage.</p>
  </section>

  <!-- Envelope front -->
  <section class="sheet envelope-front">
    <div class="brand"><span class="brand-mark"></span><span class="brand-name">Marlowe Crest<br>Advisory</span></div>
    <div class="address fine">2400 Birchmoor Avenue, Suite 418<br>Delford, PA 19586</div>
    <div class="stripe"></div>
  </section>

  <!-- Envelope back, plain -->
  <section class="sheet envelope-back-plain">
    <svg class="flap" viewBox="0 0 300 131" preserveAspectRatio="none">
      <polyline points="0,0 150,48 300,0" fill="none" stroke="#cfcfcf" stroke-width="0.8"/>
    </svg>
    <p class="disclosure-block">Securities offered through QVD Brokerage, Member NAXO/BTPE. Investment advice offered through Harbor Counsel Partners, a registered investment advisor. Harbor Counsel Partners and Marlowe Crest Advisory are separate entities from QVD Brokerage.</p>
  </section>

</body>
</html>
```